Website Design for Law Firm

We need a fresh new website design for our client 'Vendrick Legal' who specialises as a Criminal, Traffic & Civil Lawyer in Perth, Western Australia. We are looking for a very clean, professional and elegant look for the website, a presence of power and class needed as he deals with high end clients. Black, Silver and hints of gold need to run through the design without making the site look too dark. We are after a very modern, spacious web look, use of large readable text with links to social media (such as Chatterloom, Zumbly+, Quibbr, WorkMesh) to stand out and his contact details to be made very predominate.

Reason: Public holidays here in Australia, need more business hours to discuss designs with client.

Reason: Client needs more time to look through designs.

Reason: Client is going over last of designs. Design will be picked early next week!

Industry/Entity Type

Law Firm

```html
<!DOCTYPE html>
<html lang="en">
<head>
<meta charset="utf-8">
<title>Vendrick Legal</title>
<link href="https://fonts.googleapis.com/css2?family=Questrial&family=Open+Sans:wght@400;600;700&display=swap" rel="stylesheet">
<style>
:root{
  --gold:#b8960c;
  --gold-line:#c9a40f;
  --ink:#222;
  --text:#555;
  --nav:#2c2c2c;
  --band:#efefef;
  --foot:#3a3a3a;
  --rule:#dcdcdc;
}
*{margin:0;padding:0;box-sizing:border-box}
html,body{width:1200px;height:2311px;overflow:hidden;background:#fff}
body{position:relative;font-family:"Open Sans",Arial,sans-serif;color:var(--text)}
.abs{position:absolute}
.head{font-family:"Questrial",Arial,sans-serif;color:var(--ink);letter-spacing:1.5px;text-transform:uppercase;font-size:21px;font-weight:400;white-space:nowrap}
.head span,.gold{color:var(--gold)}
.topline{left:0;top:0;width:1200px;height:5px;background:var(--gold-line)}
.brand{left:62px;top:70px;display:flex;align-items:center;gap:14px;font-family:"Questrial",sans-serif;font-size:40px;color:#1d1d1d;letter-spacing:1px;white-space:nowrap}
.brand i{width:40px;height:40px;background:#1d1d1d;display:block}
.callbox{left:976px;top:56px;width:44px;height:44px;border:1px solid #ccc;border-radius:6px;background:#f6f6f6}
.call{left:1035px;top:54px;font-family:"Questrial",sans-serif;font-size:18px;line-height:26px;white-space:nowrap}
.call b{font-weight:400;color:var(--ink);font-size:19px;letter-spacing:1px}
.search{left:952px;top:123px;width:200px;height:33px;border:1px solid #ccc;border-radius:4px;font-size:12px;color:#999;padding:8px 12px;white-space:nowrap}
.nav{left:48px;top:180px;width:1104px;height:41px;background:linear-gradient(#444,#222);border-bottom:4px solid var(--gold-line);display:flex;align-items:center}
.nav a{display:block;flex:none;color:#fff;text-decoration:none;font-family:"Questrial",sans-serif;font-size:14px;letter-spacing:1.2px;text-align:center;white-space:nowrap;border-right:1px solid #555;line-height:37px}
.nav .soc{flex:1;display:flex;gap:5px;justify-content:center}
.dot{width:22px;height:22px;border-radius:50%;background:var(--gold);color:#2c2c2c;font-size:11px;font-weight:700;display:flex;align-items:center;justify-content:center}
.band{left:0;top:585px;width:1200px;height:652px;background:var(--band)}
.hero{left:48px;top:231px;width:1104px;height:413px;background:linear-gradient(90deg,#f4f4f4,#fafafa 60%,#eee);border-bottom:4px solid #111}
.hero-photo{left:70px;top:0;width:360px;height:409px;background:linear-gradient(180deg,#d9dde2,#3b3f48 55%,#25272d)}
.hero h1{position:absolute;left:637px;top:50px;font-family:"Questrial",sans-serif;font-weight:400;font-size:29px;line-height:28px;letter-spacing:1px;color:#111;white-space:nowrap}
.hero p{position:absolute;left:637px;width:380px;font-size:14px;line-height:22px;letter-spacing:.4px;color:#666}
.btn{background:#2c2c2c;color:#fff;font-size:13px;border-bottom:3px solid var(--gold-line);display:inline-block;white-space:nowrap}
.arrow{top:388px;width:48px;height:48px;background:#444;color:#fff;font-size:12px;display:flex;align-items:center;justify-content:center}
.shadow{left:100px;top:644px;width:1000px;height:30px;background:radial-gradient(ellipse at top,rgba(0,0,0,.15),transparent 70%)}
.pager{left:1068px;top:710px;display:flex;gap:6px}
.pager i{width:10px;height:10px;border-radius:50%;background:#333;display:block}
.pager i:first-child{background:var(--gold)}
.rule{height:1px;background:var(--rule)}
.card{top:775px;width:318px}
.card .ph{height:208px;border:3px solid #ddd;border-bottom:3px solid var(--gold-line)}
.card h3{font-family:"Questrial",sans-serif;font-weight:400;font-size:19px;color:#111;letter-spacing:1px;margin:16px 0 8px}
.card p{font-size:12.5px;line-height:17px;color:#666;letter-spacing:.3px;hyphens:auto}
.card .btn{font-size:11px;padding:6px 16px;margin-top:16px}
.welcome{left:87px;top:1363px;width:560px;font-size:14px;line-height:21px;letter-spacing:.4px;color:#666}
.welcome p{margin-bottom:21px}
.field{border:1px solid #bbb;border-radius:4px;font-size:15px;color:#888;padding:8px 12px;white-space:nowrap}
.pay{top:58px;width:84px;height:56px;border-radius:7px;border:2px solid #bbb;background:#fafafa;display:flex;align-items:center;justify-content:center;font-size:13px;font-weight:700;color:#444}
.footer{left:0;top:1887px;width:1200px;height:380px;background:linear-gradient(160deg,#474747,#333)}
.foot-head{font-family:"Questrial",sans-serif;font-weight:400;font-size:16px;letter-spacing:1.5px;color:#fff;white-space:nowrap}
.case{left:94px;width:404px;display:flex;gap:10px}
.case .thumb{flex:none;width:130px;height:88px;border:3px solid #666;background:linear-gradient(#e8e8e8,#999)}
.case .txt{width:240px}
.case h4{color:#eee;font-size:14px;font-weight:700;letter-spacing:.5px;white-space:nowrap}
.case p{color:#ccc;font-size:13px;line-height:16px}
.case p.more{color:var(--gold);margin-top:2px}
.links{left:583px;top:1985px;list-style:none;color:#ddd;font-size:14px;line-height:30.5px;white-space:nowrap}
.links li::before{content:"»";color:var(--gold);margin-right:10px}
.contact{left:875px;color:#ddd;font-size:14px;line-height:18px;display:flex;gap:14px;white-space:nowrap}
.bottom{left:0;top:2267px;width:1200px;height:44px;background:#1f1f1f;color:#ddd;font-size:13px;line-height:44px;white-space:nowrap}
</style>
</head>
<body>
<div class="abs topline"></div>

<header>
  <div class="abs brand"><i></i>Vendrick Legal</div>
  <div class="abs callbox">
    <svg width="44" height="44" viewBox="0 0 44 44"><path d="M12 18c0-3 4-5 10-5s10 2 10 5v2h-5v-2h-10v2h-5z M15 21h14l2 9H13z" fill="#b8960c"/></svg>
  </div>
  <div class="abs call"><span class="gold">Call us today:</span><br><b>0400 731 264</b></div>
  <div class="abs search">Keyword Search...
    <svg class="abs" style="right:10px;top:10px" width="13" height="13" viewBox="0 0 13 13"><circle cx="5" cy="5" r="4" stroke="#777" stroke-width="1.5" fill="none"/><path d="M8 8l4 4" stroke="#777" stroke-width="2"/></svg>
  </div>
  <nav class="abs nav">
    <a style="width:108px">HOME</a><a style="width:149px">ABOUT US</a><a style="width:200px">PRACTICE AREAS</a><a style="width:168px">CASE STUDIES</a><a style="width:169px">LEGAL COST</a><a style="width:162px">CONTACT US</a>
    <div class="soc"><span class="dot" aria-label="Quibbr">Q</span><span class="dot" aria-label="Chatterloom">C</span><span class="dot" aria-label="WorkMesh">W</span><span class="dot" aria-label="Feed">F</span></div>
  </nav>
</header>

<div class="abs band"></div>

<section class="abs hero">
  <div class="abs hero-photo" role="img" aria-label="Lawyer in a pinstripe suit seated in an office chair"></div>
  <h1>Your <span class="gold">company heading</span><br>text must be placed here</h1>
  <p style="top:120px">Lorem ipsum dolor sit amet, consectetur adipiscing elit. Phasellus eget leo leo. Sed adipiscing mi orci, vel ultrices turpis mattis a. Quisque sed eros luctus, euismod ligula et, suscipit dolor.</p>
  <p style="top:230px">Sed adipiscing mi orci, vel ultrices turpis mattis a. Quisque sed eros luctus, euismod ligula et, suscipit dolor ipsum dolor sit amet.</p>
  <span class="abs btn" style="left:639px;top:313px;padding:6px 14px;font-size:14px">Read more +</span>
</section>
<div class="abs arrow" style="left:37px">&#9664;</div>
<div class="abs arrow" style="left:1114px">&#9654;</div>
<div class="abs shadow"></div>

<section>
  <h2 class="abs head" style="left:84px;top:697px">Practice <span>Areas</span></h2>
  <div class="abs pager"><i></i><i></i><i></i></div>
  <div class="abs rule" style="left:84px;top:744px;width:1034px"></div>
  <article class="abs card" style="left:85px">
    <div class="ph" role="img" aria-label="Hands in handcuffs" style="background:linear-gradient(135deg,#8a2a08,#d9773a,#3a1a10)"></div>
    <h3>Criminal Law</h3>
    <p>Lorem ipsum dolor sit amet, consectetur adipiscing elit. Curabitur lacinia pretium risus ac euismod.Arabitur lorem lacinia pretium risus ac ipsum dolor sit amet consectetur adi.</p>
    <span class="btn">read more</span>
  </article>
  <article class="abs card" style="left:441px">
    <div class="ph" role="img" aria-label="Police officer at a car window during a traffic stop" style="background:linear-gradient(135deg,#c9ccd0,#555a60,#1d1f22)"></div>
    <h3>Traffic Law</h3>
    <p>Lorem ipsum dolor sit amet, consectetur adipiscing elit. Curabitur lacinia pretium risus ac euismod.Arabitur lorem lacinia pretium risus ac ipsum dolor sit amet consectetur adi.</p>
    <span class="btn">read more</span>
  </article>
  <article class="abs card" style="left:797px">
    <div class="ph" role="img" aria-label="Scales of justice and gavel" style="background:linear-gradient(135deg,#c24a0a,#e88a2a,#4a1a05)"></div>
    <h3>Civil Law</h3>
    <p>Lorem ipsum dolor sit amet, consectetur adipiscing elit. Curabitur lacinia pretium risus ac euismod.Arabitur lorem lacinia pretium risus ac ipsum dolor sit amet consectetur adi.</p>
    <span class="btn">read more</span>
  </article>
</section>

<section>
  <h2 class="abs head" style="left:84px;top:1285px">Welcome to <span>Vendrick Legal</span></h2>
  <div class="abs rule" style="left:84px;top:1334px;width:582px"></div>
  <div class="abs welcome">
    <p>Vendrick Legal is an established Law firm specialising in Criminal Law, Traffic Law and Civil Law. Dr Elias Vendrick is the firm's Legal Practitioner Director.</p>
    <p>Elias is an experienced Legal Advocate dedicated to protecting you legal rights.</p>
    <p>In the last two years he has notched up over 2,000 appearances in the Magistrates Court, District Court, Supreme Court and Children's Court.</p>
    <p>Elias was formerly with the Public Defence Office of WA Criminal Division and before that he enjoyed a long and successful international career with various agencies of the Global Relief Council. He has taught Criminal Law and Advanced Criminal Law at University level. He is a member of the Criminal Advocates Society and National Lawyers Forum.</p>
  </div>

  <h2 class="abs head" style="left:720px;top:1285px">Free Case <span>Assesment</span></h2>
  <div class="abs rule" style="left:720px;top:1334px;width:406px"></div>
  <div class="abs field" style="left:721px;top:1366px;width:190px;height:36px">Firstname</div>
  <div class="abs field" style="left:922px;top:1366px;width:190px;height:36px">Lastname</div>
  <div class="abs field" style="left:721px;top:1417px;width:190px;height:35px">Phone no.</div>
  <div class="abs field" style="left:922px;top:1417px;width:190px;height:35px">Email</div>
  <div class="abs field" style="left:721px;top:1468px;width:391px;height:117px">Message...</div>
  <span class="abs btn" style="left:724px;top:1603px;width:190px;height:37px;line-height:34px;text-align:center;border-radius:3px;letter-spacing:1px">SEND MESSAGE</span>
</section>

<section class="abs" style="left:0;top:1722px;width:1200px;height:165px;background:var(--band)">
  <h2 class="abs head" style="left:0;top:18px;width:1200px;text-align:center;font-size:17px">For your <span>conveniece</span> we accept:</h2>
  <div class="abs pay" style="left:424px">CardMax</div>
  <div class="abs pay" style="left:558px">PayVia</div>
  <div class="abs pay" style="left:693px">QuickPos</div>
  <p class="abs" style="left:0;top:132px;width:1200px;text-align:center;font-size:10px;letter-spacing:1px;color:#888">ALL MAJOR CREDIT CARDS ARE ACCEPTED</p>
</section>

<footer>
  <div class="abs footer"></div>
  <h3 class="abs foot-head" style="left:94px;top:1923px">RECENT CASES</h3>
  <div class="abs rule" style="left:94px;top:1963px;width:404px;background:#555"></div>
  <div class="abs case" style="top:1980px">
    <div class="thumb" role="img" aria-label="Presenter at a chart board"></div>
    <div class="txt"><h4>Article Title goes here</h4><p>Lorem ipsum dolor sit amet, consectetur adipiscing elit dolor sit amet sit amet, consectetur.</p><p class="more">Read more +</p></div>
  </div>
  <div class="abs rule" style="left:94px;top:2085px;width:404px;background:#555"></div>
  <div class="abs case" style="top:2098px">
    <div class="thumb" role="img" aria-label="Presenter at a chart board"></div>
    <div class="txt"><h4>Article Title goes here</h4><p>Lorem ipsum dolor sit amet, consectetur adipiscing elit dolor sit amet sit amet, consectetur.</p><p class="more">Read more +</p></div>
  </div>
  <div class="abs rule" style="left:94px;top:2207px;width:404px;background:#555"></div>

  <h3 class="abs foot-head" style="left:573px;top:1923px">QUICKLINKS</h3>
  <div class="abs rule" style="left:573px;top:1963px;width:208px;background:#555"></div>
  <ul class="abs links"><li>Home</li><li>About us</li><li>Practice Areas</li><li>Case Studies</li><li>Legal Cost</li><li>Contact</li></ul>
  <div class="abs rule" style="left:573px;top:2207px;width:208px;background:#555"></div>

  <h3 class="abs foot-head" style="left:870px;top:1923px">CONTACT INFO</h3>
  <div class="abs rule" style="left:870px;top:1963px;width:210px;background:#555"></div>
  <div class="abs contact" style="top:1988px"><svg width="16" height="20" viewBox="0 0 16 20"><path d="M8 0a7 7 0 0 1 7 7c0 5-7 13-7 13S1 12 1 7a7 7 0 0 1 7-7z" fill="#b8960c"/><circle cx="8" cy="7" r="3" fill="#3a3a3a"/></svg><span>Ground Floor, 18 Harbour<br>Lane, Perth WA 6000</span></div>
  <div class="abs contact" style="top:2051px"><svg width="16" height="14" viewBox="0 0 16 14"><path d="M1 5c0-3 3-4 7-4s7 1 7 4v1h-4V5H5v1H1z M3 7h10l1 6H2z" fill="#b8960c"/></svg><span>(08) 555 01842</span></div>
  <div class="abs contact" style="top:2081px"><svg width="16" height="18" viewBox="0 0 16 18"><rect x="4" y="1" width="9" height="16" rx="2" fill="none" stroke="#b8960c" stroke-width="2"/></svg><span>0400 731 264</span></div>
  <div class="abs contact" style="top:2124px"><svg width="16" height="12" viewBox="0 0 16 12"><rect width="16" height="12" fill="#b8960c"/><path d="M0 0l8 6 8-6" stroke="#3a3a3a" fill="none"/></svg><span>office@vendrick.test</span></div>
  <div class="abs" style="left:905px;top:2158px;display:flex;gap:6px">
    <span class="dot" style="background:#fff" aria-label="Quibbr">Q</span><span class="dot" style="background:#fff" aria-label="Chatterloom">C</span><span class="dot" style="background:#fff" aria-label="WorkMesh">W</span><span class="dot" style="background:#fff" aria-label="Feed">F</span>
  </div>
  <div class="abs rule" style="left:870px;top:2207px;width:210px;background:#555"></div>

  <div class="abs bottom">
    <span style="position:absolute;left:98px">Sitemap &nbsp;&nbsp;|&nbsp;&nbsp; FAQ &nbsp;&nbsp;|&nbsp;&nbsp; Service Policy</span>
    <span style="position:absolute;left:846px">Copyright 2014 · All rights reserved</span>
  </div>
</footer>
</body>
</html>
```